Stationary for Beauty and Spa School

Create a business card, letterhead and envelopes (primarily #10 envelope with and without window and catalog envelope) for a beauty and wellness school in Miami, Fl. We offer 8 different programs of study and need an eye catching look. Looking for a combination of modern yet sophisticated. Nothing corporate or business looking. Would like to have a look and feel that is similar (or incorporates aspects) of a new website we will be launching in the next 30 days (screen shot attached.)

The final design should communicate style and elegance in a down to earth and friendly way. We strive to provide our students with quality education, friendly and amicable staff and experienced instructors.
Updates

Hello. FYI, in order to print an aesthetically appealing business card, we would like to print them (the business cards) using silk printing method, with spot UV coating (on some elements, maybe the logo, or depending on the design) and die cuts. Please think of this when preparing your design.

Only 1 day left, please submit your designs for selection. Thanks

Target Market(s)

Adults 18-49 years who are mostly interested in beauty and fashion. Need a youthful & modern look, yet sophisticated and elegant.

Industry/Entity Type

School

Colors
e34197
6b449b
add136
f79021

Requirements
Must have
• Similar look and feel as website (see attached screen shot)
Same look and feel of website (see attached screenshot)
Logo
Address: 5216 SW 3rd Avenue. Miami, Fl 33155
Telephone: 305-514-9382
Fax: 786-420-5163
website/url: www.luminora.edu
incorporate Photo of blonde model (attached)
Nice to have
• Tag line: "Beautify your future." Also, maybe two-sided business card. Would be nice if we could mention our programs (maybe in the back of the card). Below are the program offerings (names cannot be changed but order is irrelevant)... Cosmetology, Barber, Spa Therapy, Massage Therapy, Makeup Artistry, Skin Care, Manicure, Pedicure & Nail Extensions, Full Specialist.

A design with text plus a beautiful photo of a model is appealing. Attached to the files is a sample of a cover for a student handbook we have created. You should use the photo of the blonde model (attached) in your design. The original (quality) version of this stock photograph has been uploaded.

Also would be nice to request clients to follow us on facebook and instagram by including the icons.
Should not have
• A corporate or business look. We are a vocational school teaching beauty and spa programs and we like our advertising to have a look that resembles the industry. We do not want a very serious look or snobby feel.

```html
<!DOCTYPE html>
<html lang="en">
<head>
<meta charset="utf-8">
<title>Luminora School of Beauty — Stationery</title>
<link rel="stylesheet" href="https://fonts.googleapis.com/css2?family=Didact+Gothic&family=Raleway:ital,wght@1,300&family=Dancing+Script:wght@400&family=Great+Vibes&display=swap">
<style>
  :root {
    --backdrop: #c3c5c7;
    --paper: #ffffff;
    --envelope: #ececec;
    --band: #141414;
    --ink: #3a3a3a;
    --ink-dark: #111111;
    --muted: #8a8a8a;
    --faint: #dcdcdc;
    --signature: #1d2a6b;
    --lime: #add136;
    --stamp: #a8835a;
    --on-dark: #ffffff;
  }
  * { margin: 0; padding: 0; box-sizing: border-box; }
  html, body { width: 1200px; height: 1000px; overflow: hidden; }
  body { background: var(--backdrop); font-family: "Didact Gothic", sans-serif; color: var(--ink); }
  .canvas { position: relative; width: 1200px; height: 1000px; }

  /* Shared logotype */
  .logotype { position: absolute; color: var(--on-dark); font-family: "Didact Gothic", sans-serif; font-weight: 400; line-height: 1; }
  .logotype .name { display: block; letter-spacing: 1px; }
  .logotype .sub { display: block; letter-spacing: 0.5px; }
  .tagline { position: absolute; font-family: "Raleway", sans-serif; font-style: italic; font-weight: 300; color: var(--muted); white-space: nowrap; }

  /* Letterhead */
  .letterhead { position: absolute; left: 111px; top: 145px; width: 496px; height: 699px; background: var(--paper); }
  .letterhead .band { position: absolute; left: 0; top: 0; width: 100%; height: 75px; background: var(--band); }
  .letterhead .logotype { left: 16px; top: 12px; }
  .letterhead .logotype .name { font-size: 40px; }
  .letterhead .logotype .sub { font-size: 12px; margin: 8px 0 0 50px; }
  .letterhead .tagline { right: 2px; top: 56px; font-size: 16px; }
  .letterhead .watermark { position: absolute; left: 62px; top: 312px; font-size: 62px; color: var(--faint); letter-spacing: 2px; }
  .letter-body { position: absolute; left: 59px; top: 165px; width: 376px; font-size: 12.2px; line-height: 15px; text-align: justify; color: var(--ink); }
  .letter-body p { text-indent: 22px; margin-bottom: 15px; }
  .signoff { position: absolute; left: 324px; top: 556px; }
  .signoff .printed { font-size: 14px; color: var(--ink-dark); }
  .signoff .signed { font-family: "Great Vibes", cursive; font-size: 20px; color: var(--signature); margin: 6px 0 0 10px; }
  .letter-footer { position: absolute; left: 0; bottom: 0; width: 100%; height: 40px; font-size: 12px; color: var(--ink-dark); }
  .letter-footer .label { font-family: "Dancing Script", cursive; font-size: 12px; color: var(--ink); margin-right: 6px; }
  .letter-footer .address { position: absolute; left: 108px; top: 0; }
  .letter-footer .phone { position: absolute; left: 11px; top: 19px; }
  .letter-footer .fax { position: absolute; left: 187px; top: 19px; }
  .letter-footer .web { position: absolute; left: 347px; top: 19px; }

  /* Envelope, back */
  .envelope { position: absolute; left: 734px; width: 405px; background: var(--envelope); }
  .envelope-back { top: 148px; height: 178px; }
  .envelope-back .flap { position: absolute; left: 0; top: 0; width: 405px; height: 26px; }
  .envelope-back .watermark { position: absolute; left: 112px; top: 80px; color: #d6d6d6; line-height: 1; }
  .envelope-back .watermark .name { display: block; font-size: 40px; letter-spacing: 1px; }
  .envelope-back .watermark .sub { display: block; font-size: 11px; margin: 4px 0 0 48px; }

  /* Envelope, front */
  .envelope-front { top: 359px; height: 177px; }
  .envelope-front .band { position: absolute; left: 0; top: 0; width: 100%; height: 39px; background: var(--band); }
  .envelope-front .logotype { left: 12px; top: 6px; }
  .envelope-front .logotype .name { font-size: 20px; }
  .envelope-front .logotype .sub { font-size: 7px; margin: 3px 0 0 26px; }
  .envelope-front .stamp { position: absolute; left: 358px; top: 9px; width: 34px; height: 38px; background: linear-gradient(135deg, #c7a57c, var(--stamp)); border: 2px solid #efe6d8; }
  .envelope-front .recipient { position: absolute; left: 0; top: 95px; width: 100%; text-align: center; font-size: 15px; line-height: 18px; color: var(--ink-dark); letter-spacing: 0.5px; }

  /* Business cards */
  .card { position: absolute; left: 733px; width: 216px; height: 127px; background: var(--band); color: var(--on-dark); }
  .card-front { top: 568px; }
  .card-front .logotype { left: 44px; top: 14px; }
  .card-front .logotype .name { font-size: 27px; }
  .card-front .logotype .sub { font-size: 8px; margin: 5px 0 0 34px; }
  .card-front .tagline { left: 108px; top: 58px; font-size: 8px; color: #9a9a9a; }
  .card-contacts { position: absolute; left: 40px; top: 81px; font-size: 6px; line-height: 9.5px; }
  .card-contacts .row { display: flex; }
  .card-contacts .label { width: 32px; text-align: right; padding-right: 4px; font-family: "Dancing Script", cursive; color: #bdbdbd; }
  .card-back { top: 717px; }
  .programs { position: absolute; left: 0; top: 10px; width: 100%; text-align: center; font-family: "Dancing Script", cursive; font-size: 7.2px; line-height: 9.3px; color: var(--lime); list-style: none; }
  .social { position: absolute; top: 103px; font-size: 6.2px; color: var(--lime); display: flex; align-items: center; gap: 2px; }
  .social .mark { width: 7px; height: 7px; background: var(--lime); }
  .social-first { left: 16px; }
  .social-second { left: 120px; }
</style>
</head>
<body>
<main class="canvas">

  <section class="letterhead" aria-label="Letterhead">
    <div class="band"></div>
    <div class="logotype"><span class="name">Luminora</span><span class="sub">SCHOOL OF BEAUTY</span></div>
    <div class="tagline">Beautify your future</div>
    <div class="watermark" aria-hidden="true">Luminora</div>
    <div class="letter-body">
      <p>Lorem ipsum dolor sit amet, consectetuer adipiscing elit, sed diam nonummy nibh euismod tincidunt ut laoreet dolore magna aliquam erat volutpat. Ut wisi enim ad minim veniam, quis nostrud exerci tation ullamcorper suscipit lobortis nisl ut aliquip ex ea commodo consequat.</p>
      <p>Duis autem vel eum iriure dolor in hendrerit in vulputate velit esse molestie consequat, vel illum dolore eu feugiat nulla facilisis at vero eros et accumsan et iusto odio dignissim qui blandit praesent luptatum zzril delenit augue duis dolore te feugait nulla facilisi.</p>
      <p>Nam liber tempor cum soluta nobis eleifend option congue nihil imperdiet doming id quod mazim placerat facer possim assum. Typi non habent claritatem insitam; est usus legentis in iis qui facit eorum claritatem. Investigationes demonstraverunt lectores legere me lius quod ii legunt saepius. Claritas est etiam processus dynamicus, qui sequitur mutationem consuetudium lectorum.</p>
      <p>Mirum est notare quam littera gothica, quam nunc putamus parum claram, anteposuerit litterarum formas humanitatis per seacula quarta decima et quinta decima. Eodem modo typi, qui nunc nobis videntur parum clari, fiant sollemnes in futurum.</p>
    </div>
    <div class="signoff">
      <div class="printed">Jane Doe</div>
      <div class="signed">Jane Doe</div>
    </div>
    <footer class="letter-footer">
      <span class="address"><span class="label">address</span>5216 SW 3rd Avenue. Miami, Fl 33155</span>
      <span class="phone"><span class="label">phone</span>305-514-9382</span>
      <span class="fax"><span class="label">fax</span>786-420-5163</span>
      <span class="web"><span class="label">web</span>www.luminora.edu</span>
    </footer>
  </section>

  <section class="envelope envelope-back" aria-label="Envelope, back">
    <svg class="flap" viewBox="0 0 405 26" aria-hidden="true">
      <path d="M0 0 H405 V16 Q402 22 390 22 H15 Q3 22 0 16 Z" fill="#141414"/>
    </svg>
    <div class="watermark" aria-hidden="true"><span class="name">Luminora</span><span class="sub">SCHOOL OF BEAUTY</span></div>
  </section>

  <section class="envelope envelope-front" aria-label="Envelope, front">
    <div class="band"></div>
    <div class="logotype"><span class="name">Luminora</span><span class="sub">SCHOOL OF BEAUTY</span></div>
    <div class="stamp" role="img" aria-label="Postage stamp"></div>
    <div class="recipient">5216 SW 3rd Avenue.<br>Miami, Fl 33155</div>
  </section>

  <section class="card card-front" aria-label="Business card, front">
    <div class="logotype"><span class="name">Luminora</span><span class="sub">SCHOOL OF BEAUTY</span></div>
    <div class="tagline">Beautify your future</div>
    <div class="card-contacts">
      <div class="row"><span class="label">address</span>5216 SW 3rd Avenue. Miami, Fl 33155</div>
      <div class="row"><span class="label">phone</span>305-514-9382</div>
      <div class="row"><span class="label">fax</span>786-420-5163</div>
      <div class="row"><span class="label">web</span>www.luminora.edu</div>
    </div>
  </section>

  <section class="card card-back" aria-label="Business card, back">
    <ul class="programs">
      <li>Cosmetology</li>
      <li>Barber</li>
      <li>Spa Therapy</li>
      <li>Massage Therapy</li>
      <li>Makeup Artistry</li>
      <li>Skin Care</li>
      <li>Manicure</li>
      <li>Pedicure &amp; Nail Extensions</li>
      <li>Full Specialist</li>
    </ul>
    <div class="social social-first"><span class="mark"></span>luminorabeautyschool</div>
    <div class="social social-second"><span class="mark"></span>luminorabeautyschool</div>
  </section>

</main>
</body>
</html>
```